pvt business card

need clean and modern business card design, possibly two. Logo on front and writing on back-Full source files for logo attached-THE CHOSEN LOGO IS SQUARE PVT with PVT HOLDINGS in ALL BLUE. Please do not use any other logos from files, this is source file that includes correct logo

```html
<!DOCTYPE html>
<html lang="en">
<head>
<meta charset="utf-8">
<title>PVT Holdings – Business Card</title>
<link rel="stylesheet" href="https://fonts.googleapis.com/css2?family=Michroma&family=Roboto:wght@400;500&display=swap">
<style>
  :root {
    --stage: #1f2024;
    --brand-blue: #3a7cc4;
    --ink-blue: #3571bd;
    --accent-green: #8dc63f;
    --paper: #ffffff;
    --faint: rgba(255,255,255,0.10);
  }
  * { margin: 0; padding: 0; box-sizing: border-box; }
  html, body { width: 1200px; height: 800px; overflow: hidden; }
  body {
    background: var(--stage);
    display: flex;
    align-items: center;
    justify-content: center;
    gap: 40px;
  }
  .card {
    position: relative;
    width: 525px;
    height: 300px;
    border-radius: 18px;
    overflow: hidden;
  }
  /* Front */
  .card--front { background: var(--brand-blue); color: var(--paper); }
  .front-decor {
    position: absolute;
    left: -70px; top: 90px;
    width: 300px; height: 300px;
  }
  .front-brand {
    position: absolute;
    inset: 0;
    display: flex;
    flex-direction: column;
    align-items: center;
    justify-content: center;
    gap: 10px;
  }
  .front-brand .mark-dot {
    width: 62px; height: 62px;
    border: 7px solid var(--paper);
    border-radius: 50%;
    margin-bottom: 8px;
  }
  .brand-name {
    font-family: "Michroma", sans-serif;
    font-size: 30px;
    letter-spacing: 1px;
    line-height: 1;
  }
  .brand-tagline {
    font-family: "Michroma", sans-serif;
    font-size: 9.5px;
    letter-spacing: 0.6px;
  }
  /* Back */
  .card--back { background: var(--paper); }
  .back-mark {
    position: absolute;
    right: 38px; top: 48px;
    width: 150px; height: 150px;
    border: 12px solid var(--ink-blue);
    border-radius: 50%;
  }
  .back-info {
    position: absolute;
    left: 36px; top: 60px;
  }
  .back-info .brand-name { color: var(--ink-blue); font-size: 24px; }
  .back-info .brand-tagline { color: var(--accent-green); font-size: 8px; margin-top: 5px; }
  .person { margin-top: 32px; }
  .person-name {
    font-family: "Michroma", sans-serif;
    font-size: 13px;
    color: var(--ink-blue);
  }
  .person-role {
    font-family: "Roboto", sans-serif;
    font-size: 12px;
    color: var(--accent-green);
    margin-top: 3px;
  }
  .contact {
    margin-top: 16px;
    font-family: "Roboto", sans-serif;
    font-size: 11.5px;
    color: var(--ink-blue);
    line-height: 1.5;
    list-style: none;
  }
  .contact li { display: flex; align-items: center; gap: 6px; }
  .contact svg { width: 11px; height: 11px; fill: var(--accent-green); flex: none; }
  .contact .indent { padding-left: 17px; }
  .web {
    margin-top: 4px;
    font-family: "Roboto", sans-serif;
    font-size: 11.5px;
    font-weight: 500;
    letter-spacing: 2.5px;
    color: var(--ink-blue);
  }
  .web span { color: var(--accent-green); }
</style>
</head>
<body>
  <section class="card card--front" aria-label="Card front">
    <svg class="front-decor" viewBox="0 0 300 300" aria-hidden="true">
      <circle cx="150" cy="150" r="130" fill="none" stroke="rgba(255,255,255,0.10)" stroke-width="26"/>
    </svg>
    <div class="front-brand">
      <div class="mark-dot"></div>
      <div class="brand-name">PVT HOLDINGS</div>
      <div class="brand-tagline">PARKVALE TRADING GROUP</div>
    </div>
  </section>

  <section class="card card--back" aria-label="Card back">
    <div class="back-mark"></div>
    <div class="back-info">
      <div class="brand-name">PVT HOLDINGS</div>
      <div class="brand-tagline">PARKVALE TRADING GROUP</div>
      <div class="person">
        <div class="person-name">DANIEL REYES</div>
        <div class="person-role">Director</div>
      </div>
      <ul class="contact">
        <li class="indent">PO BOX 456, Elm Road</li>
        <li class="indent">4th Lane, Oregon</li>
        <li>
          <svg viewBox="0 0 24 24"><path d="M6.6 10.8a15.1 15.1 0 0 0 6.6 6.6l2.2-2.2a1 1 0 0 1 1-.25 11.4 11.4 0 0 0 3.6.57 1 1 0 0 1 1 1V20a1 1 0 0 1-1 1A17 17 0 0 1 3 4a1 1 0 0 1 1-1h3.5a1 1 0 0 1 1 1c0 1.25.2 2.45.57 3.57a1 1 0 0 1-.25 1z"/></svg>
          (555) 218 4097
        </li>
        <li>
          <svg viewBox="0 0 24 24"><path d="M2 5h20v14H2z M2 5l10 8 10-8" /></svg>
          info@pvtmail.com
        </li>
      </ul>
      <div class="web">www.<span>pvtholdings</span>.com</div>
    </div>
  </section>
</body>
</html>
```